TheGlowFrame.net

TheGlowFrame.net
Open Globe Snap Salon of pictures of love for all to enjoy
My goal is to create a website that is designed to be an online art gallery of photos that display what love looks like from all over the world. People will submit an image; write a short quote about why their image represents love
I Love THIS website:
http://markwellory.example/
Please create something like this!!!
User Functionality:
Users must be able to do the following:
• Upload one photo
• Write a brief quote
• Share on their social media site
• Other users can like and share posted image
Backend:
• Site owner must be able to choose which images are uploaded. After user uploads image to site, admin will receive notice of the upload, and make sure the image is not unappropriated or spam. That would be the control functionality.
• At the bottom of the site a contact us, that will send e-mail to admin for any user related questions
Design Functionality:
Website should only be one, simple, elegant, page of photos.
Social Media:
Social media buttons should be small, at the corner of each submitted image
I Love THIS website:
http://markwellory.example/
Homepage: I like the layout and design you have now. Each square/image will have the following social media options, friendloop,chirpline,and Snapgrid. Below each photo their will be a caption that described each photo that appears after you hover over the photo, camera equipment, and a link to the photographer's portfolio/website. There will be able 30-40 images at a time on the homepage, 5-7 photographers at a time.
Featured Photographers:
This is the second page of the website. Here there is a bio of the photographers, how to contact them, and where in the world they are from. The photographers will always be on the page even after their work is taken off the homepage. I will insert links to their personal websites under their bio.
Review/Shop:
Here I will be using affiliated marketing to sell cameras, camera accessories, online photo classes, frames. I will not be selling the pictures featured on the homepage, people will be able to buy directly from the photographer.
Selling: I will be using brimhall partners, and tap vault. I will be installing CoinDrift, but all sales will be they third party vendors
Contact Us:
Here people can inquire about becoming a featured photographer, the company, and anything else
Site Requirements:
Email visitors can join the company mail group.
Target Market(s)
photographers, people who like snapgrid, and boardly
Industry/Entity Type
Marketing
Look and feel

```html
<!DOCTYPE html>
<html lang="en">
<head>
<meta charset="utf-8">
<title>The Glow Frame</title>
<link rel="stylesheet" href="https://fonts.googleapis.com/css2?family=Asap:ital,wght@0,600;0,700;1,600&family=Ubuntu:wght@300;400&family=Roboto:wght@400;700&display=swap">
<style>
  :root {
    --page: #efefef;
    --white: #ffffff;
    --ink: #3a3a3a;
    --muted: #6d6d6d;
    --accent: #f4363f;
    --share: #f06a5e;
    --share-active: #3f8fd2;
    --contact: #0a8ac8;
    --rule: #d6d6d6;
    --dark: #1c1c1c;
  }
  * { box-sizing: border-box; margin: 0; padding: 0; }
  html, body { width: 894px; height: 1200px; overflow: hidden; }
  body { position: relative; background: var(--page); font-family: "Roboto", Arial, sans-serif; color: var(--ink); }

  .site-header { position: absolute; left: 0; top: 0; width: 894px; height: 48px; background: var(--white); }
  .brand { position: absolute; left: 46px; top: 11px; font-family: "Asap", sans-serif; font-weight: 700; font-size: 23px; color: #4a4a4a; }
  .main-nav { position: absolute; left: 564px; top: 0; display: flex; height: 48px; }
  .main-nav a { display: block; height: 48px; line-height: 50px; padding: 0 11px; font-size: 10.5px; color: #222; text-decoration: none; text-transform: uppercase; }
  .main-nav a.is-current { background: var(--accent); color: var(--white); width: 50px; text-align: center; }

  .hero { position: absolute; left: 44px; top: 76px; width: 806px; height: 244px; overflow: hidden; background: linear-gradient(100deg, #8fc0dc 0%, #d8c2ae 22%, #eef3f7 38%, #4b8fc0 58%, #a9d3ee 78%, #e6f2fa 100%); }
  .hero-caption { position: absolute; right: 0; bottom: 0; width: 458px; height: 134px; background: rgba(255,255,255,0.55); padding: 30px 14px 0 0; text-align: right; white-space: nowrap; font-family: "Ubuntu", sans-serif; font-weight: 300; font-size: 26px; letter-spacing: -0.3px; line-height: 42px; color: #2b2b2b; }

  .card { position: absolute; background: var(--white); }
  .card-photo { display: block; width: 100%; }
  .tone-mono-a { background: linear-gradient(160deg, #9a9a9a, #3c3c3c 55%, #b8b8b8); }
  .tone-mono-b { background: linear-gradient(120deg, #d8d8d8, #6a6a6a 50%, #2e2e2e); }
  .tone-mono-c { background: linear-gradient(180deg, #5d5d5d, #c9c9c9 60%, #8a8a8a); }
  .tone-mono-d { background: linear-gradient(140deg, #e4e4e4, #7b7b7b 45%, #cfcfcf); }
  .tone-mono-e { background: linear-gradient(90deg, #bdbdbd, #3e3e3e 55%, #6f6f6f); }
  .tone-warm { background: linear-gradient(110deg, #6a4a3a, #c89a82 35%, #3a2a22 65%, #8a6a5a); }

  .card-body { position: relative; padding: 12px 10px 0 12px; }
  .card-title { font-family: "Asap", sans-serif; font-style: italic; font-weight: 600; font-size: 13.6px; letter-spacing: -0.2px; line-height: 18px; color: var(--ink); }
  .card-title.is-highlight { color: var(--accent); }
  .card-meta { position: absolute; left: 12px; bottom: 12px; display: flex; align-items: center; font-size: 9px; color: var(--muted); }
  .card-meta svg { margin-right: 5px; }
  .card-meta .count { margin-right: 14px; }
  .share { position: absolute; right: 12px; bottom: 11px; }

  .upload { position: absolute; left: 595px; top: 342px; width: 253px; height: 112px; background: var(--accent); }
  .upload-button { position: absolute; left: 25px; top: 24px; width: 203px; height: 64px; background: #ededed; border: 4px solid var(--white); box-shadow: 0 1px 3px rgba(0,0,0,0.35); font-family: "Ubuntu", sans-serif; font-size: 17px; letter-spacing: -0.3px; white-space: nowrap; line-height: 56px; text-align: center; color: #333; }

  .footer-rule { position: absolute; left: 0; top: 1028px; width: 894px; height: 1px; background: var(--rule); }
  .contact { position: absolute; left: 44px; top: 1045px; width: 806px; height: 127px; background: var(--contact); color: var(--white); }
  .contact-heading { position: absolute; left: 20px; top: 13px; font-size: 18px; font-weight: 400; }
  .field { position: absolute; top: 53px; width: 160px; }
  .field label { display: block; font-size: 9.5px; height: 9px; margin-bottom: 8px; }
  .field .input { display: block; width: 160px; height: 29px; background: var(--white); }
  .submit { position: absolute; left: 706px; top: 57px; width: 78px; height: 36px; background: var(--dark); border: 2px solid var(--white); box-shadow: 2px 2px 3px rgba(0,0,0,0.4); font-family: "Roboto", sans-serif; font-weight: 700; font-size: 16px; line-height: 32px; text-align: center; color: var(--white); }
</style>
</head>
<body>

<header class="site-header">
  <div class="brand">The Glow Frame</div>
  <nav class="main-nav">
    <a class="is-current" href="#">Home</a>
    <a href="#">About</a>
    <a href="#">Gallery</a>
    <a href="#">Blog</a>
    <a href="#">Contacts</a>
  </nav>
</header>

<section class="hero" role="img" aria-label="Couple relaxing together in bright blue daylight">
  <div class="hero-caption">Open Globe Snap Salon of Pictures<br>of Love for all to Enjoy</div>
</section>

<svg width="0" height="0" style="position:absolute">
  <defs>
    <symbol id="icon-comment" viewBox="0 0 10 9"><path d="M5 0C2.2 0 0 1.6 0 3.6c0 1.1.7 2 1.7 2.7L1.2 9l2.5-1.7c.4.1.9.1 1.3.1 2.8 0 5-1.6 5-3.6S7.8 0 5 0z" fill="#555"/></symbol>
    <symbol id="icon-share" viewBox="0 0 10 10"><circle cx="8" cy="2" r="2"/><circle cx="2" cy="5" r="2"/><circle cx="8" cy="8" r="2"/><path d="M8 2L2 5l6 3" stroke-width="1.2" fill="none"/></symbol>
  </defs>
</svg>

<article class="card" style="left:46px; top:342px; width:253px; height:257px;">
  <div class="card-photo tone-mono-a" style="height:170px;" role="img" aria-label="Black and white photo of a couple lying in the grass"></div>
  <div class="card-body" style="height:87px;">
    <p class="card-title">Lorem ipsum dolor sit amet conse<br>ctetur adipisicing elit.</p>
    <div class="card-meta"><svg width="9" height="8"><use href="#icon-comment"/></svg><span class="count">1</span><span>30 May, 11:32</span></div>
    <svg class="share" width="9" height="9" fill="var(--share)" stroke="var(--share)"><use href="#icon-share"/></svg>
  </div>
</article>

<article class="card" style="left:46px; top:622px; width:253px; height:364px;">
  <div class="card-photo tone-mono-b" style="height:253px;" role="img" aria-label="Black and white photo of a laughing couple embracing"></div>
  <div class="card-body" style="height:111px;">
    <p class="card-title">Duis aute irure dolor in reprehenderit<br>in voluptate velit esse cillum dolore<br>eu fugiat nulla.</p>
    <div class="card-meta"><svg width="9" height="8"><use href="#icon-comment"/></svg><span class="count">1</span><span>30 May, 11:32</span></div>
    <svg class="share" width="9" height="9" fill="var(--share)" stroke="var(--share)"><use href="#icon-share"/></svg>
  </div>
</article>

<article class="card" style="left:319px; top:341px; width:256px; height:365px;">
  <div class="card-photo tone-warm" style="height:253px;" role="img" aria-label="Close colour portrait of a couple"></div>
  <div class="card-body" style="height:112px;">
    <p class="card-title is-highlight">Duis aute irure dolor in reprehenderit<br>in voluptate velit esse cillum dolore<br>eu fugiat nulla.</p>
    <div class="card-meta"><svg width="9" height="8"><use href="#icon-comment"/></svg><span class="count">1</span><span>30 May, 11:32</span></div>
    <svg class="share" width="9" height="9" fill="var(--share-active)" stroke="var(--share-active)"><use href="#icon-share"/></svg>
  </div>
</article>

<article class="card" style="left:319px; top:728px; width:256px; height:258px;">
  <div class="card-photo tone-mono-c" style="height:172px;" role="img" aria-label="Black and white photo of a couple walking among trees"></div>
  <div class="card-body" style="height:86px;">
    <p class="card-title">Lorem ipsum dolor sit amet conse<br>ctetur adipisicing elit.</p>
    <div class="card-meta"><svg width="9" height="8"><use href="#icon-comment"/></svg><span class="count">1</span><span>30 May, 11:32</span></div>
    <svg class="share" width="9" height="9" fill="var(--share)" stroke="var(--share)"><use href="#icon-share"/></svg>
  </div>
</article>

<div class="upload"><div class="upload-button">UPLOAD YOUR PHOTO</div></div>

<article class="card" style="left:595px; top:475px; width:253px; height:257px;">
  <div class="card-photo tone-mono-d" style="height:171px;" role="img" aria-label="Black and white photo of a couple reading a book together"></div>
  <div class="card-body" style="height:86px;">
    <p class="card-title">Lorem ipsum dolor sit amet conse<br>ctetur adipisicing elit.</p>
    <div class="card-meta"><svg width="9" height="8"><use href="#icon-comment"/></svg><span class="count">1</span><span>30 May, 11:32</span></div>
    <svg class="share" width="9" height="9" fill="var(--share)" stroke="var(--share)"><use href="#icon-share"/></svg>
  </div>
</article>

<article class="card" style="left:595px; top:754px; width:253px; height:232px;">
  <div class="card-photo tone-mono-e" style="height:151px;" role="img" aria-label="Black and white photo of a couple with a camera"></div>
  <div class="card-body" style="height:81px;">
    <p class="card-title">Reprehenderit in voluptate velit esse<br>cillum dolore eu fugiat nulla.</p>
    <div class="card-meta"><svg width="9" height="8"><use href="#icon-comment"/></svg><span class="count">1</span><span>30 May, 11:32</span></div>
    <svg class="share" width="9" height="9" fill="var(--share)" stroke="var(--share)"><use href="#icon-share"/></svg>
  </div>
</article>

<div class="footer-rule"></div>

<section class="contact">
  <h2 class="contact-heading">CONTACT US:</h2>
  <div class="field" style="left:21px;"><label>Name:</label><span class="input"></span></div>
  <div class="field" style="left:192px;"><label>Address:</label><span class="input"></span></div>
  <div class="field" style="left:365px;"><label>E-mail:</label><span class="input"></span></div>
  <div class="field" style="left:538px;"><label>Massage:</label><span class="input"></span></div>
  <div class="submit">Submit</div>
</section>

</body>
</html>
```